We need a need two-page flyer that talks about the services of Bright Harbour. We like this created in ppt if possible (let me know if not). We have created the BH ppt for your reference. Please use the attached Oldharbour .pdf for reference. We like this to be fun and creative in flair and style. Something that the sales people can use and will wow the client if we email it to them.

```html
<!DOCTYPE html>
<html lang="en">
<head>
<meta charset="utf-8">
<title>Bright Harbour – Event Management Flyer</title>
<link href="https://fonts.googleapis.com/css2?family=PT+Sans:ital,wght@0,400;0,700;1,400&display=swap" rel="stylesheet">
<style>
:root{
  --navy:#16287a;
  --blue:#2a55b8;
  --heading:#1d4ea3;
  --sky:#7fb6e6;
  --text:#3a3a3a;
  --page:#ffffff;
  --backdrop:#e9e9eb;
}
*{box-sizing:border-box;margin:0;padding:0}
html,body{width:1200px;height:783px;overflow:hidden;background:var(--backdrop);font-family:"PT Sans",sans-serif;color:var(--text)}
.canvas{position:relative;width:1200px;height:783px}
.page{position:absolute;top:48px;width:519px;height:672px;background:var(--page);box-shadow:0 2px 8px rgba(0,0,0,.18);overflow:hidden}
.page--services{left:70px}
.page--approach{left:620px}
.hero{position:absolute;left:0;top:0}
.brand{position:absolute;display:flex;align-items:center;gap:8px}
.brand__mark{width:26px;height:26px;background:var(--blue)}
.brand__name{font-size:22px;font-weight:400;color:#333;letter-spacing:.5px}
.title-bar{position:absolute;left:0;height:28px;padding:0 14px 0 18px;display:flex;align-items:center;color:#fff;font-size:14px;background:linear-gradient(90deg,var(--navy),var(--blue));border-radius:0 14px 14px 0;box-shadow:2px 2px 0 #c9d6ee}
.tagline{position:absolute;left:18px;top:240px;font-style:italic;font-size:11.5px;color:#222}
.service{position:absolute;left:24px;width:478px;height:69px;display:flex;gap:22px}
.service__photo{flex:0 0 142px;height:69px}
.service h3{font-size:10px;color:var(--heading);font-weight:700;margin-bottom:1px}
.service p{font-size:7.6px;line-height:1.2;text-align:justify}
.col{position:absolute}
.col h3{font-size:11px;color:var(--heading);font-weight:700;margin-bottom:6px}
.col p{font-size:7.8px;line-height:1.25;text-align:justify}
.bullets{list-style:none}
.bullets li{position:relative;padding-left:13px;font-size:7.8px;line-height:1.27;text-align:justify;margin-bottom:8px}
.bullets li::before{content:"";position:absolute;left:0;top:2px;width:7px;height:7px;border-radius:50%;background:var(--heading)}
.company{position:absolute;left:18px;top:584px}
.company__name{font-style:italic;font-size:13.5px;color:#333;margin-bottom:5px}
.company__address{font-size:11px;color:#333;line-height:1.15}
.footer{position:absolute;left:0;bottom:0;width:100%;height:32px;background:linear-gradient(90deg,var(--blue),var(--navy) 55%,var(--blue));display:flex;align-items:center;justify-content:space-between;padding:0 18px 0 22px;color:#fff;font-size:9.5px}
.footer__item{display:flex;align-items:center;gap:6px}
.footer svg{width:12px;height:12px}
</style>
</head>
<body>
<div class="canvas">

  <section class="page page--services">
    <svg class="hero" width="519" height="260" viewBox="0 0 519 260">
      <defs>
        <linearGradient id="heroA" x1="0" y1="0" x2="1" y2="1">
          <stop offset="0" stop-color="#1e5a6a"/><stop offset=".5" stop-color="#3ea4c8"/><stop offset="1" stop-color="#0f2a4a"/>
        </linearGradient>
      </defs>
      <path d="M0,0 H519 V218 C380,250 200,220 0,168 Z" fill="url(#heroA)" role="img" aria-label="Photo of a shipwreck themed event room lit in blue with a ship wheel and foliage"/>
      <path d="M0,0 H225 C205,50 150,85 0,92 Z" fill="#fff"/>
      <path d="M0,168 C200,220 380,250 519,218 V232 C380,262 200,236 0,182 Z" fill="#2a55b8"/>
      <path d="M0,182 C200,236 380,262 519,232 V238 C380,268 200,244 0,188 Z" fill="#9cc4ec"/>
    </svg>
    <div class="brand" style="left:22px;top:26px"><span class="brand__mark"></span><span class="brand__name">BRIGHT HARBOUR</span></div>
    <div class="title-bar" style="top:206px">EVENT MANAGEMENT SERVICES</div>
    <p class="tagline">Bringing People, Businesses, Markets And Ideas Together</p>

    <div class="service" style="top:272px">
      <div class="service__photo" role="img" aria-label="Photo of a themed prop booth at an event" style="background:linear-gradient(135deg,#8a7a5c,#c9b48c 50%,#4a3a2a)"></div>
      <div><h3>Themed Props and Décor</h3><p>At Bright Harbour we are known for providing décor that completely changes the surrounds of your venue and provides your guests with an immersive event experience. Our expert event designers understand how the product will be used and where it will be most impactful. Whether being transported to outer space or to a tropical paradise, our props drive each theme home. We also will use foliage, lighting, ice, and even custom décor items</p></div>
    </div>
    <div class="service" style="top:344px">
      <div class="service__photo" role="img" aria-label="Photo of a purple lit LED dance floor" style="background:linear-gradient(180deg,#5a2a9a,#c07ae8 60%,#3a1a6a)"></div>
      <div><h3>Harbour Lights</h3><p>Harbour Lights was born from the need to eliminate pesky cords at our events. Our lighted décor is now completely battery operated. We now sell most of our lights to multiple companies and theme parks throughout the United States. Our lighted products are brand friendly, meaning we can add a logo or monogram to just about any of our lighted décor items.</p></div>
    </div>
    <div class="service" style="top:416px">
      <div class="service__photo" role="img" aria-label="Photo of tropical palms and foliage around a carved totem" style="background:linear-gradient(135deg,#2f6a22,#7fbf3a 50%,#244a18)"></div>
      <div><h3>Harbour Greens</h3><p>Harbour Greens is our only company that is not located on property. We have 40,000 square feet of green houses with a large selection of inventory from 14' Amstel Ficus Trees, 12' Palms, to lush Boston Ferns and many more in between.</p></div>
    </div>
    <div class="service" style="top:489px">
      <div class="service__photo" role="img" aria-label="Photo of a drink being poured through an ice sculpture luge" style="background:linear-gradient(135deg,#3a2a22,#b08a6a 50%,#1a1a2a)"></div>
      <div><h3>Carving Ice</h3><p>Ice sculptures are a central point and unique statement at a corporate event or wedding. Ice will attract attention and provide a memorable focal and visual for attendee discussion. It can even be an interactive experience when your guests use an ice luge for the first time or drink from a glass with a large ice cube featuring your logo!</p></div>
    </div>
    <div class="service" style="top:561px">
      <div class="service__photo" role="img" aria-label="Photo of an evening street event with lit trees and tents" style="background:linear-gradient(135deg,#4a3a1a,#d8b060 45%,#6a1a1a)"></div>
      <div><h3>Custom Fabrication for All Types of Events</h3><p>At Bright Harbour our in-house fabrication team has the ability to deliver custom designs and fabrications that will make your next event a unique one. Our team of professionals specializes in providing creative event solutions for companies planning both in-office and off-site activities. Our services provide the very best in custom staging, furniture and décor, scenic displays, tradeshow booths, and much more.</p></div>
    </div>

    <footer class="footer">
      <span class="footer__item"><svg viewBox="0 0 12 12"><circle cx="6" cy="6" r="5.5" fill="none" stroke="#fff"/><rect x="3" y="4" width="6" height="4" fill="none" stroke="#fff" stroke-width=".8"/><path d="M3,4 L6,6.3 L9,4" fill="none" stroke="#fff" stroke-width=".8"/></svg>hello@brightharbour.com</span>
      <span class="footer__item"><svg viewBox="0 0 12 12"><circle cx="6" cy="6" r="5.5" fill="none" stroke="#fff"/><path d="M4,3.5 L5,3.2 L5.6,4.8 L5,5.3 Q5.6,6.6 6.7,7 L7.2,6.4 L8.8,7 L8.5,8 Q5,8.4 4,3.5 Z" fill="#fff"/></svg>(555) 014-2270</span>
      <span class="footer__item"><svg viewBox="0 0 12 12"><circle cx="6" cy="6" r="5.5" fill="none" stroke="#fff"/><ellipse cx="6" cy="6" rx="2" ry="4" fill="none" stroke="#fff" stroke-width=".7"/><path d="M2,6 H10" stroke="#fff" stroke-width=".7"/></svg>www.brightharbour.com</span>
    </footer>
  </section>

  <section class="page page--approach">
    <svg class="hero" width="519" height="300" viewBox="0 0 519 300">
      <defs>
        <linearGradient id="heroB" x1="0" y1="0" x2="1" y2="1">
          <stop offset="0" stop-color="#1a1410"/><stop offset=".45" stop-color="#6a4a2a"/><stop offset=".7" stop-color="#c8c8d0"/><stop offset="1" stop-color="#2a2020"/>
        </linearGradient>
      </defs>
      <path d="M0,0 H519 V250 C420,290 300,300 150,260 C90,244 40,226 0,214 Z" fill="url(#heroB)" role="img" aria-label="Photo of a banquet table with clear chairs beneath vintage aircraft in a hangar"/>
      <path d="M0,214 C40,226 90,244 150,260 C300,300 420,290 519,250 V266 C420,306 290,312 150,274 C90,258 40,240 0,228 Z" fill="#2a55b8"/>
      <path d="M519,266 C420,306 290,312 150,274 V280 C290,318 420,312 519,272 Z" fill="#9cc4ec"/>
    </svg>
    <div class="brand" style="left:18px;top:244px"><span class="brand__mark"></span><span class="brand__name">BRIGHT HARBOUR</span></div>
    <div class="title-bar" style="top:298px">Our Approach to a Successful Event</div>

    <div class="col" style="left:18px;top:342px;width:226px">
      <h3>An Extension of Your Own team</h3>
      <ul class="bullets">
        <li>When you employ Bright Harbour to create or manage one of your events, you can be assured that you are in the safe hands of thoroughbred event organizers.</li>
        <li>We like to work as an extension of your own company, treating your events and brands as respectfully as we do our own and consulting carefully on all significant decisions.</li>
        <li>We have a strong understanding of budget constraints, constantly monitoring expenditure commitments and managing the various risks involved.</li>
        <li>We use our extensive supplier and venue relationships to keep your costs low whilst ensuring the highest quality, with many clients finding that using our services is more cost-effective than running their events through an in-house team.</li>
      </ul>
    </div>

    <div class="company">
      <p class="company__name">Bright Harbour</p>
      <p class="company__address">412 Quayside Lane,<br>Port Elden, FL 30991</p>
    </div>

    <div class="col" style="left:262px;top:342px;width:236px">
      <h3>About us</h3>
      <p>Founded in 1999, Bright Harbour is a specialist organizer of business-to-business events, including conferences, award ceremonies, seminars, workshops, roadshows, roundtables and exhibitions for the public, commercial and third sectors.</p>
    </div>
    <div class="col" style="left:262px;top:428px;width:236px">
      <h3>Budget transparency</h3>
      <p>We always work to a pre-agreed budget and a pre-agreed management fee, based on the amount of sales, marketing and logistical time needed to manage your event.</p>
      <p style="margin-top:10px">Your final bill will not differ from this pre-agreed amount unless there have been significant changes to the project along the way.</p>
    </div>
    <div class="col" style="left:262px;top:548px;width:236px">
      <h3 style="margin-bottom:3px">Meet the team</h3>
      <p>Organizing professional events requires a significant amount of time and 'attention-to-detail' across a whole range of different disciplines – but we endeavor to provide a single point of contact to streamline client communications wherever possible.</p>
    </div>

    <footer class="footer">
      <span class="footer__item"><svg viewBox="0 0 12 12"><circle cx="6" cy="6" r="5.5" fill="none" stroke="#fff"/><rect x="3" y="4" width="6" height="4" fill="none" stroke="#fff" stroke-width=".8"/><path d="M3,4 L6,6.3 L9,4" fill="none" stroke="#fff" stroke-width=".8"/></svg>hello@brightharbour.com</span>
      <span class="footer__item"><svg viewBox="0 0 12 12"><circle cx="6" cy="6" r="5.5" fill="none" stroke="#fff"/><path d="M4,3.5 L5,3.2 L5.6,4.8 L5,5.3 Q5.6,6.6 6.7,7 L7.2,6.4 L8.8,7 L8.5,8 Q5,8.4 4,3.5 Z" fill="#fff"/></svg>(555) 014-2270</span>
      <span class="footer__item"><svg viewBox="0 0 12 12"><circle cx="6" cy="6" r="5.5" fill="none" stroke="#fff"/><ellipse cx="6" cy="6" rx="2" ry="4" fill="none" stroke="#fff" stroke-width=".7"/><path d="M2,6 H10" stroke="#fff" stroke-width=".7"/></svg>www.brightharbour.com</span>
    </footer>
  </section>

</div>
</body>
</html>
```